I am looking to make a tri fold brochure for my company called The Brightway Hub for Emergency Training & Event Safety. This tri fold should specifically target the education setting and offering CPR Workshops and Assembly Programs in schools for children, teachers and staff of all ages.

You can visit our company website www.brightwayhubtraining.example to learn more under our training tab. I am also attaching a version I tried to make myself. It doesn't have to be quite like that...but I want it stand out and grab the attention of the reader! The files attached are for you to play with...anything relevant is fine.

TEXT TO BE USED:
The Brightway Hub for Emergency Training & Event Safety is ready and willing to come to your school today! Set up your personalized training programs from private classroom workshops, large assemblies programs or for sports teams and faculty meetings. Be the school district that goes above and beyond. CPR/AED & First Aid Training makes a great subject for 21st century learning!

Schools are excellent places to offer CPR training, whether it's for graduation requirements, to help students with after-school or summer job requirements, or simply to improve cardiac survival rates in their community. When you teach kids CPR in schools you are strengthening community safety and giving students skills they can carry into the future for a lifetime.

Random Bullets/Facts:
Approved program through Halvern CORDA Arts in Education

A bystander who administers CPR to a sudden cardiac arrest victim can as much as triple the victims chances of survival. Since 4 out of 5 cardiac arrests happen at home, there is a good chance a rescuer will be helping his or her own loved one.

New York State has become the 19th state to sign Rescue Ready Youth Bill which will make it mandatory for all high-school students to be trained in CPR and learn how to use automated defibrillators under legislation signed by Governor Peter Lindqvist.

NYS Education Law Section 917, enacted in May 2002, requires public school officials and school administrators to ensure the presence of at least 1 automated external defibrillator installed in each school, as well as an appropriately trained, certified individuals in CPR who can respond to an emergency.

Contact Us!
555.204.6139
Milo@brightwayhubtraining.example
www.brightwayhubtraining.example

Industry/Entity Type

Education

```html
<!DOCTYPE html>
<html lang="en">
<head>
<meta charset="utf-8">
<title>The Brightway Hub – School CPR Tri-fold</title>
<link rel="stylesheet" href="https://fonts.googleapis.com/css2?family=Roboto+Condensed:wght@300;400;700&family=Oswald:wght@500&family=Courier+Prime&family=Open+Sans:wght@400;700&display=swap">
<style>
:root{
  --red:#d0202e;
  --red-dark:#a8131e;
  --black:#0d0d0d;
  --white:#ffffff;
  --paper:#f4f4f4;
  --gray:#7a7a7a;
  --gray-dark:#4d4d4d;
  --teal:#2fb7c6;
  --ink:#1d1d1d;
}
*{box-sizing:border-box;margin:0;padding:0}
html,body{width:800px;height:1200px;overflow:hidden;background:#ffffff}
body{position:relative;font-family:"Roboto Condensed",sans-serif;color:var(--ink)}
.sheet{position:absolute;left:20px;width:760px;height:520px;display:grid;grid-template-columns:repeat(3,1fr);box-shadow:0 6px 18px rgba(0,0,0,.18)}
.sheet--outside{top:30px}
.sheet--inside{top:640px}
.panel{position:relative;overflow:hidden}
.photo{display:block;width:100%}
/* outside, panel 1 */
.law-panel{background:var(--red);color:var(--white)}
.law-panel .photo{height:245px;background:linear-gradient(180deg,#cfd6d4 0%,#9aa7a8 45%,#b9a99a 100%)}
.ribbon{position:absolute;top:232px;left:38px;width:178px;height:34px;background:var(--teal);color:var(--white);font-weight:300;font-size:22px;text-align:center;line-height:34px;letter-spacing:.5px}
.law-text{padding:40px 14px 0 14px;font-weight:300;font-size:15.5px;line-height:1.3;text-align:justify}
/* outside, panel 2 */
.contact-panel{background:var(--white)}
.hero{position:relative;height:130px;margin:10px 10px 4px;background:linear-gradient(160deg,#d8d8d8,#8d8d8d 60%,#c4222c)}
.hero-text{position:absolute;left:8px;bottom:14px;font-family:"Open Sans",sans-serif;font-size:13px;font-weight:700;line-height:1.25}
.hero-text .accent{color:var(--red)}
.tile-grid{display:grid;grid-template-columns:1fr 1fr;gap:4px;margin:0 10px}
.tile-grid .photo{height:102px}
.tile-a{background:linear-gradient(150deg,#8fb4d6,#d9c9b8)}
.tile-b{background:linear-gradient(150deg,#6b2b25,#d4b54a)}
.tile-c{background:linear-gradient(150deg,#4f6f9a,#c9c3b2)}
.tile-d{background:linear-gradient(150deg,#3e3a5e,#8d6fb0)}
.contact{margin-top:38px;text-align:center;font-size:13.5px;font-weight:700;line-height:1.3;font-style:normal}
/* outside, panel 3 */
.cover-panel{background:var(--white)}
.brand-bar{background:var(--black);height:72px;display:flex;align-items:center;justify-content:center;color:var(--white)}
.brand-name{font-weight:700;font-size:22px;line-height:1;color:var(--white)}
.cover-panel .photo{height:150px;background:linear-gradient(170deg,#c9b9ae,#7d6f6a 60%,#3b3fa8)}
.mission{font-family:"Courier Prime",monospace;color:var(--red);font-size:14px;text-align:center;line-height:1.25;padding:10px 8px 0}
.partner{display:flex;align-items:center;justify-content:center;gap:6px;margin-top:12px;font-size:10px;font-weight:700;line-height:1.1}
.partner-mark{width:22px;height:22px;border-radius:50%;background:var(--red);flex:none}
.corner{position:absolute;left:0;bottom:0;width:100%;height:120px}
.banner{position:absolute;left:14px;font-weight:300;font-size:20px;color:var(--white);padding:2px 8px;white-space:nowrap}
.banner--red{bottom:66px;background:var(--red);border:1px solid var(--white)}
.banner--black{bottom:32px;left:24px;background:var(--black);border:1px solid var(--white)}
/* inside, panel 1 */
.student-panel{background:linear-gradient(180deg,#8a8a8a,#5d5d5d);color:var(--white)}
.student-panel .photo{height:230px;background:linear-gradient(160deg,#9a7a6a,#d8c2b0 50%,#4c6fae)}
.logo-bar{margin:12px 16px 0;background:var(--black);height:38px;display:flex;align-items:center;justify-content:center}
.logo-bar .brand-name{font-size:19px}
.caption{font-size:9.5px;font-style:italic;text-align:right;padding:6px 14px 0;line-height:1.25}
.schools-text{padding:12px 14px 0;font-weight:300;font-size:14.5px;line-height:1.22;text-align:justify}
/* inside, panels 2 and 3 */
.programs{grid-column:2 / span 2;background:var(--paper);display:grid;grid-template-columns:1fr 1fr;grid-template-rows:auto 1fr}
.programs-head{grid-column:1 / span 2;padding:14px 16px 6px}
.programs-title{font-size:21px;font-weight:400;text-align:center;letter-spacing:.3px}
.programs-text{color:var(--red);font-weight:300;font-size:12.5px;line-height:1.25;text-align:justify;margin-top:6px}
.ready-col{padding:4px 12px 0;position:relative}
.ready{font-family:"Oswald",sans-serif;color:var(--red);font-size:25px;line-height:1;text-align:center}
.ready small{font-size:16px}
.ready-sub{font-family:"Oswald",sans-serif;font-size:16px;text-align:center;color:var(--black)}
.skyline{height:38px;margin-top:6px;background:linear-gradient(180deg,#f4f4f4,#1a1a1a)}
.chain-title{font-family:"Oswald",sans-serif;color:var(--red);font-size:22px;text-align:center;margin-top:6px}
.chain{display:flex;justify-content:center;margin-top:6px}
.chain svg{display:block}
.chain-labels{display:flex;justify-content:space-around;font-size:6.5px;color:var(--red);margin-top:2px}
.next-gen{position:relative;display:flex;align-items:flex-end;gap:8px;margin-top:12px;border-bottom:4px solid var(--red);padding-bottom:4px}
.next-figures{width:70px;height:62px;background:linear-gradient(90deg,#555,#bbb)}
.next-text{font-size:10px;line-height:1}
.next-text strong{display:block;font-family:"Oswald",sans-serif;color:var(--red);font-size:22px;line-height:.95}
.aed-col{padding:4px 14px 0}
.aed-col .photo{height:118px;background:linear-gradient(90deg,#c23a3a 0%,#d84a4a 45%,#e9e9e6 46%,#cfd4c0 100%)}
.fact{color:var(--red);font-weight:300;font-size:14px;line-height:1.25;text-align:justify;margin-top:10px}
.council{display:flex;align-items:center;justify-content:center;gap:10px;margin-top:18px;font-size:21px;font-weight:300;color:var(--black)}
.council .partner-mark{width:30px;height:30px}
.council-tag{text-align:center;font-weight:300;font-size:18px;margin-top:6px}
</style>
</head>
<body>

<section class="sheet sheet--outside" aria-label="Brochure outside">
  <div class="panel law-panel">
    <div class="photo" role="img" aria-label="Photo of a classroom with CPR training manikins laid out on the floor"></div>
    <div class="ribbon">BE CPR SMART</div>
    <p class="law-text">NYS Education Law Section 917, enacted in May 2002, requires public school officials and school administrators to ensure the presence of at least 1 automated external defibrillator installed in each school, as well as an appropriately trained, certified individuals in CPR who can respond to an emergency.</p>
  </div>

  <div class="panel contact-panel">
    <div class="hero" role="img" aria-label="Photo of cupped hands holding a red heart">
      <p class="hero-text">Get CPR trained.<br><span class="accent">Save a LIFE</span></p>
    </div>
    <div class="tile-grid">
      <div class="photo tile-a" role="img" aria-label="Photo of hands doing chest compressions on a manikin"></div>
      <div class="photo tile-b" role="img" aria-label="Photo of students with training manikins"></div>
      <div class="photo tile-c" role="img" aria-label="Photo of a sports team at a CPR session"></div>
      <div class="photo tile-d" role="img" aria-label="Photo of a student holding a manikin"></div>
    </div>
    <address class="contact">
      Contact Us!<br>
      27 Marlow Lane Easton, NY 11590<br>
      555.204.6139<br>
      Milo@brightwayhubtraining.example<br>
      www.brightwayhubtraining.example
    </address>
  </div>

  <div class="panel cover-panel">
    <header class="brand-bar">
      <div class="brand-name">The Brightway Hub</div>
    </header>
    <div class="photo" role="img" aria-label="Photo of people practising CPR on manikins"></div>
    <p class="mission">The Brightway Hub is a leading provider of safety and emergency preparedness training center</p>
    <div class="partner">
      <span class="partner-mark"></span>
      <span>Cardiac Care Council<br>Stroke Care Council</span>
    </div>
    <svg class="corner" viewBox="0 0 253 120" preserveAspectRatio="none" aria-hidden="true">
      <polygon points="0,20 60,0 253,120 0,120" fill="var(--red)"/>
    </svg>
    <div class="banner banner--red">THE NEXT LIFE SAVED</div>
    <div class="banner banner--black">COULD BE YOURS...</div>
  </div>
</section>

<section class="sheet sheet--inside" aria-label="Brochure inside">
  <div class="panel student-panel">
    <div class="photo" role="img" aria-label="Photo of smiling students practising CPR on manikins"></div>
    <div class="logo-bar"><div class="brand-name">The Brightway Hub</div></div>
    <p class="caption">Students will learn life long skills that very well one day save someones life. Whoknows...maybe it will be yours?</p>
    <p class="schools-text">Schools are excellent places to offer CPR training, whether it's for graduation requirements, to help students with after-school or summer job requirements, or simply to improve cardiac survival rates in their community. When you teach kids CPR in schools you are strengthening community safety and giving students skills they can carry into the future for a lifetime.</p>
  </div>

  <div class="programs">
    <div class="programs-head">
      <h2 class="programs-title">TRAINING PROGRAMS FOR SCHOOLS</h2>
      <p class="programs-text">The Brightway Hub for Emergency Training &amp; Event Safety is ready and willing to come to your school today! Set up your personalized training programs from private classroom workshops, large assemblies programs or for sports teams and faculty meetings. Be the school district that goes above and beyond. CPR/AED &amp; First Aid Training makes a great subject for 21st century learning!</p>
    </div>

    <div class="ready-col">
      <p class="ready">Ready <small>for an</small><br>Emergency?</p>
      <p class="ready-sub">You can be.</p>
      <div class="skyline" role="img" aria-label="Silhouette illustration of emergencies: fire, storm, city and waves"></div>
      <h3 class="chain-title">THE SURVIVAL CHAIN</h3>
      <div class="chain">
        <svg width="200" height="50" viewBox="0 0 200 50" aria-hidden="true">
          <g fill="none" stroke="#9a9a9a" stroke-width="3">
            <circle cx="26" cy="25" r="22"/><circle cx="75" cy="25" r="22"/><circle cx="124" cy="25" r="22"/><circle cx="173" cy="25" r="22"/>
          </g>
          <g fill="var(--red)">
            <circle cx="26" cy="25" r="15"/><circle cx="75" cy="25" r="15"/><circle cx="124" cy="25" r="15"/><circle cx="173" cy="25" r="15"/>
          </g>
          <g fill="#fff">
            <path d="M26 32 l-7-7 a4 4 0 0 1 7-5 a4 4 0 0 1 7 5z"/>
            <path d="M75 32 l-7-7 a4 4 0 0 1 7-5 a4 4 0 0 1 7 5z"/>
            <path d="M124 32 l-7-7 a4 4 0 0 1 7-5 a4 4 0 0 1 7 5z"/>
            <path d="M173 32 l-7-7 a4 4 0 0 1 7-5 a4 4 0 0 1 7 5z"/>
          </g>
        </svg>
      </div>
      <div class="chain-labels"><span>EARLY ACCESS</span><span>EARLY CPR</span><span>EARLY DEFIBRILLATION</span><span>EARLY ADVANCED CARE</span></div>
      <div class="next-gen">
        <div class="next-figures" role="img" aria-label="Silhouettes of people walking"></div>
        <p class="next-text">Join the<strong>NEXT<br>GENERATION</strong>of Lifeline Corps Training</p>
      </div>
    </div>

    <div class="aed-col">
      <div class="photo" role="img" aria-label="Photo of a school hallway with red lockers and a wall-mounted AED cabinet"></div>
      <p class="fact">A bystander who administers CPR to a sudden cardiac arrest victim can as much as triple the victims chances of survival. Since 4 out of 5 cardiac arrests happen at home, there is a good chance a rescuer will be helping his or her own loved one.</p>
      <div class="council"><span>Cardiac Care Council</span><span class="partner-mark"></span></div>
      <p class="council-tag">Learn and Act</p>
    </div>
  </div>
</section>

</body>
</html>
```